Company Work Van Design

I am requiring designs for the company work van. The van is a White 2015 Corvane Brisk twin turbo short wheel base. I require all my details on the van. VTRA: 582 4036 M: 0471 865 302 Harbourline Waterproofing Pty Ltd, On the sides i require some dot points for examples of jobs i do. E.g Bathrooms, Balconies, Retaining Walls. Commercial, Residential. Be creative. I will keep updating the project with other details.

Industry/Entity Type

It Company

Colors
cee9f5
85cae6
34a7d8
0493ce
0356a4
3277b5
85acd3
d0dfed
ffffff

```html
<!DOCTYPE html>
<html lang="en">
<head>
<meta charset="utf-8">
<title>Harbourline Waterproofing – Van Panel</title>
<link href="https://fonts.googleapis.com/css2?family=Arvo&family=Source+Sans+3:wght@700&display=swap" rel="stylesheet">
<style>
  :root {
    --navy: #0356a4;
    --royal: #0493ce;
    --sky: #34a7d8;
    --mist: #85cae6;
    --ice: #cee9f5;
    --steel: #3277b5;
    --white: #ffffff;
    --slate: #5f6468;
  }
  html, body {
    margin: 0;
    padding: 0;
    width: 1200px;
    height: 622px;
    overflow: hidden;
    background: var(--white);
  }
  .panel {
    position: relative;
    width: 1200px;
    height: 622px;
    overflow: hidden;
  }
  .backdrop {
    position: absolute;
    inset: 0;
    background:
      radial-gradient(ellipse 640px 400px at 980px 470px, var(--white) 0%, rgba(255,255,255,0.85) 35%, rgba(255,255,255,0) 75%),
      radial-gradient(ellipse 560px 260px at 720px 200px, rgba(206,233,245,0.7) 0%, rgba(206,233,245,0) 80%),
      linear-gradient(160deg, var(--navy) 0%, var(--steel) 22%, var(--royal) 42%, var(--mist) 68%, var(--ice) 85%, var(--white) 100%);
  }
  .services {
    position: absolute;
    left: 46px;
    top: 132px;
    margin: 0;
    padding: 0;
    list-style: none;
  }
  .services li {
    position: relative;
    padding-left: 52px;
    height: 80px;
    line-height: 80px;
    font-family: "Arvo", serif;
    font-size: 52px;
    color: var(--white);
    letter-spacing: 0.5px;
    text-shadow: 0 2px 6px rgba(3, 56, 110, 0.45);
  }
  .services li::before {
    content: "";
    position: absolute;
    left: 0;
    top: 34px;
    width: 14px;
    height: 14px;
    border-radius: 50%;
    background: var(--white);
    box-shadow: 0 1px 4px rgba(3, 56, 110, 0.4);
  }
  .contact-band {
    position: absolute;
    left: 0;
    bottom: 0;
    width: 1200px;
    height: 68px;
    background: linear-gradient(180deg, var(--steel) 0%, var(--navy) 100%);
  }
  .contact-line {
    position: absolute;
    left: 14px;
    top: 0;
    height: 68px;
    line-height: 68px;
    margin: 0;
    font-family: "Source Sans 3", sans-serif;
    font-weight: 700;
    font-size: 28px;
    color: var(--white);
    white-space: nowrap;
  }
  .contact-line .sep {
    display: inline-block;
    margin: 0 26px;
  }
  .brand-card {
    position: absolute;
    left: 830px;
    top: 516px;
    width: 344px;
    height: 106px;
    background: var(--white);
    display: flex;
    align-items: center;
    justify-content: center;
    gap: 18px;
  }
  .brand-mark {
    flex: none;
    width: 52px;
    height: 52px;
    border-radius: 50%;
    background: var(--navy);
  }
  .brand-name {
    margin: 0;
    font-family: "Source Sans 3", sans-serif;
    font-weight: 700;
    font-size: 34px;
    line-height: 36px;
    color: var(--slate);
    letter-spacing: 1px;
  }
  .brand-name .sub {
    display: block;
    font-size: 20px;
    line-height: 24px;
    letter-spacing: 3.4px;
  }
</style>
</head>
<body>
  <div class="panel">
    <div class="backdrop" role="img" aria-label="Soft blue water-light background with flowing sweeps"></div>

    <ul class="services">
      <li>Bathrooms</li>
      <li>Balconies</li>
      <li>Retaining Walls</li>
      <li>Commercial</li>
      <li>Residential</li>
    </ul>

    <div class="contact-band">
      <p class="contact-line">VTRA : 582 4036<span class="sep">•</span>MOBILE : 0471 865 302</p>
    </div>

    <div class="brand-card">
      <div class="brand-mark"></div>
      <p class="brand-name">HARBOURLINE<span class="sub">WATERPROOFING</span></p>
    </div>
  </div>
</body>
</html>
```